Improved Business Card, Government Contracting

We are looking to update the design of our business cards. We would like to create a template that can be used for future employees and easy to update.

Haldecott Advisory Partners, LLC is a Service Disabled Veteran Owned Small Business with headquarters located in Quillbrook, NR. Our current website is www.hdvprt.example. We have contracts in KS and VA with expansion opportunities in various other states. Our primary line of work is within government contracting and providing consulting services to various organizations within the Bureau of Civic Readiness. We would like to project a professional image of our company that is consistent with the industry. Provided are previous versions of our business card template that shows our logo as well. We would like to make sure the information on the cards are easily noticeable .

Target Market(s)

Government Officials
Fellow Small Business Contractors
Large Business Contractors (ex. TQRB, Vellacourt Dynamics, Crest Pallow Wendry)

Industry/Entity Type

Business

Contact Information for Business Card

Paul Larkin
Office Manager
Haldecott Advisory Partners
Ph: 555.014.2738
Email: p.larkin@hdvprt.example
www.hdvprt.example

Requirements
Must have
• The business mailing address is:
• 48312 902nd Crossing
• Quillbrook, NR 00000
Nice to have
• Embossed lettering

```html
<!DOCTYPE html>
<html lang="en">
<head>
<meta charset="utf-8">
<title>Haldecott Advisory Partners – Business Card</title>
<link rel="stylesheet" href="https://fonts.googleapis.com/css2?family=Source+Sans+3:ital,wght@0,400;0,600;0,700;1,400&display=swap">
<style>
  :root {
    --navy: #262b8c;
    --yellow: #f2e600;
    --card: #f7f7f5;
    --backdrop: #d9d9d9;
    --ink: #262b8c;
  }
  * { box-sizing: border-box; margin: 0; padding: 0; }
  html, body {
    width: 1200px; height: 1200px; overflow: hidden;
    background: var(--backdrop);
    font-family: "Source Sans 3", "Segoe UI", sans-serif;
  }
  .sheet { position: relative; width: 1200px; height: 1200px; }
  .card {
    position: absolute; left: 150px; width: 900px; height: 514px;
    background: var(--card); overflow: hidden;
    box-shadow: 0 4px 14px rgba(0,0,0,.18);
  }
  .card--contact { top: 56px; }
  .card--brand { top: 630px; }
  .card__bands { position: absolute; inset: 0; width: 100%; height: 100%; }

  /* contact face */
  .identity { position: absolute; left: 56px; top: 50px; }
  .identity__tag { display: flex; align-items: center; gap: 8px; }
  .identity__icon { width: 34px; height: 34px; }
  .identity__name {
    background: var(--navy); color: #fff; font-weight: 600;
    font-size: 27px; letter-spacing: .5px; text-transform: uppercase;
    padding: 2px 40px 2px 12px; line-height: 34px;
    clip-path: polygon(0 0, 100% 0, calc(100% - 16px) 100%, 0 100%);
  }
  .identity__role { margin-left: 54px; margin-top: 4px; color: var(--ink); font-style: italic; font-size: 20px; }
  .identity__company { margin-left: 54px; color: var(--ink); font-weight: 700; font-size: 21px; }

  .contact-list { position: absolute; left: 56px; top: 195px; list-style: none; }
  .contact-list li {
    display: flex; align-items: center; gap: 22px;
    color: var(--ink); font-size: 21px; line-height: 34px;
  }
  .contact-list svg { width: 20px; height: 20px; flex: none; }

  .brand-mini {
    position: absolute; right: 56px; top: 118px; width: 280px;
    text-align: center; color: var(--navy); font-weight: 700; font-size: 30px; line-height: 1.1;
  }

  /* brand face */
  .brand-name {
    position: absolute; left: 0; right: 0; top: 140px; text-align: center;
    color: var(--navy); font-weight: 700; font-size: 62px; line-height: 1.05; letter-spacing: 1px;
  }
</style>
</head>
<body>
<main class="sheet">

  <section class="card card--contact" aria-label="Business card, contact side">
    <svg class="card__bands" viewBox="0 0 900 514" preserveAspectRatio="none" aria-hidden="true">
      <rect fill="var(--yellow)" x="0" y="396" width="700" height="34"/>
      <path fill="var(--navy)" stroke="var(--card)" stroke-width="6" d="M-5,440 H560 C605,440 610,388 665,388 H905 V520 H-5 Z"/>
    </svg>

    <div class="identity">
      <div class="identity__tag">
        <svg class="identity__icon" viewBox="0 0 34 34" aria-hidden="true">
          <rect width="34" height="34" fill="var(--navy)"/>
          <circle cx="17" cy="12" r="6" fill="#fff"/>
          <path d="M6,30 C6,21 28,21 28,30 Z" fill="#fff"/>
        </svg>
        <span class="identity__name">Paul Larkin</span>
      </div>
      <p class="identity__role">(Office Manager)</p>
      <p class="identity__company">Haldecott Advisory Partners</p>
    </div>

    <ul class="contact-list">
      <li>
        <svg viewBox="0 0 20 20" aria-hidden="true"><path fill="var(--navy)" d="M10,1 C5.6,1 3,4.2 3,7.6 C3,12.5 10,19 10,19 C10,19 17,12.5 17,7.6 C17,4.2 14.4,1 10,1 Z"/><circle cx="10" cy="7.6" r="2.8" fill="#fff"/></svg>
        <span>48312 902nd Crossing, Quillbrook, NR 00000</span>
      </li>
      <li>
        <svg viewBox="0 0 20 20" aria-hidden="true"><rect x="5" y="1" width="10" height="18" rx="2" fill="var(--navy)"/><rect x="7" y="3.5" width="6" height="11" fill="#fff"/></svg>
        <span>555.014.2738</span>
      </li>
      <li>
        <svg viewBox="0 0 20 20" aria-hidden="true"><rect x="1" y="4" width="18" height="12" fill="var(--navy)"/><path d="M1.5,4.5 L10,11 L18.5,4.5" fill="none" stroke="#fff" stroke-width="1.5"/></svg>
        <span>p.larkin@hdvprt.example</span>
      </li>
      <li>
        <svg viewBox="0 0 20 20" aria-hidden="true"><circle cx="10" cy="10" r="9" fill="var(--navy)"/><circle cx="10" cy="10" r="3.4" fill="none" stroke="#fff" stroke-width="1.8"/><path d="M13.4,7 V11.5 C13.4,13.5 16,13.5 16,11" fill="none" stroke="#fff" stroke-width="1.6"/></svg>
        <span>www.hdvprt.example</span>
      </li>
    </ul>

    <p class="brand-mini">Haldecott Advisory Partners</p>
  </section>

  <section class="card card--brand" aria-label="Business card, company side">
    <svg class="card__bands" viewBox="0 0 900 514" preserveAspectRatio="none" aria-hidden="true">
      <rect fill="var(--yellow)" x="0" y="396" width="700" height="34"/>
      <path fill="var(--navy)" stroke="var(--card)" stroke-width="6" d="M-5,440 H560 C605,440 610,388 665,388 H905 V520 H-5 Z"/>
    </svg>
    <p class="brand-name">Haldecott<br>Advisory Partners</p>
  </section>

</main>
</body>
</html>
```